Online Training company needs a new website design (Wordpress)

We are looking for a new design for our website (run on WordPress). We currently have two websites (quizmarlow.com) and (velkorlearning.com) and are trying to combine them into a single design.

The site should contain the following sections (Start Here, courses, labs, practice exams, exam vouchers, books, articles, about us).

Start Here - With so many options on our site, we think it would be a good idea to have this page that will allow us to give students an overview of our different products/services and where to start when they first find out about our company.

Courses - These are our online video courses (products), currently hosted at velkorlearning.com. Each course has its own "product page".

Labs - These are online lab environments that a student can purchase. The layout for these would be similar to a course, but the purchase option will be different (our web developer will code all the back end stuff to make it work).

Practice Exams - This will allow students to take practice questions to study for their exams.

Exam Vouchers - Students can purchase their exam vouchers here at a discounted price for their certification exams.

Books - Will link to a page that displays our books that are available on Zorvel. (Examples of the covers are attached so you can see our current designs.)

Articles - This will be our "blog" area for us to post articles each week.

About Us - A short about us page describing our company.

***
As for the design of the page itself, we like the current color scheme at velkorlearning.com, but the layout isn't working well. It was fine when we just had video courses, but as we have added new products it is becoming more and more cumbersome.

I have been looking for inspiration around the web, and saw brightfernwealth.com as a good example of trying to provide focus to new users, while breaking out various parts of a business that contains 4-6 different product lines/topics. Another example of a site we like is lessonharborweb.com.

That said, we aren't looking to simply copy either site, and are completely open to recommendations and designs you may have.

Thank you and we look forward to working with you!

```html
<!DOCTYPE html>
<html lang="en">
<head>
<meta charset="utf-8">
<title>Quiz Marlow – ServiceFrame v3 Foundations</title>
<link rel="stylesheet" href="https://fonts.googleapis.com/css2?family=Montserrat:wght@400;500;600;700&family=Orbitron:wght@500;700&display=swap">
<style>
:root{
  --navy:#1c1a4a;
  --indigo:#2b2f8f;
  --royal:#2e3aa8;
  --hero-a:#0f2c4a;
  --hero-b:#1d5b85;
  --grey-bg:#f1f1f1;
  --sky:#7ba8d8;
  --ink:#1d1d2b;
  --muted:#666a80;
  --white:#ffffff;
  --card-border:#2a2a5a;
}
*{box-sizing:border-box;margin:0;padding:0}
html,body{width:1200px;height:2344px;overflow:hidden}
body{position:relative;background:var(--white);font-family:"Montserrat",Arial,sans-serif;color:var(--ink)}
.abs{position:absolute}

/* header */
.site-header{position:absolute;left:0;top:0;width:1200px;height:120px;background:var(--white)}
.top-strip{position:absolute;left:0;top:0;width:1200px;height:6px;background:#0d0d2a}
.account-bar{position:absolute;right:0;top:0;width:525px;height:39px;background:var(--indigo);clip-path:polygon(32px 0,100% 0,100% 100%,0 100%)}
.account-link{position:absolute;top:12px;color:var(--white);font-size:13px;font-weight:700;display:flex;align-items:center;gap:8px;letter-spacing:.3px}
.brand{position:absolute;left:223px;top:48px;display:flex;align-items:center;gap:10px;font-size:22px;font-weight:700;color:var(--indigo)}
.brand-dot{width:26px;height:26px;border-radius:50%;background:var(--indigo)}
.main-nav{position:absolute;left:462px;top:65px;display:flex;gap:11px;font-size:10px;font-weight:600;color:var(--indigo);white-space:nowrap}
.main-nav .current{background:var(--indigo);color:var(--white);padding:3px 5px;margin-top:-3px}

/* hero */
.hero{position:absolute;left:0;top:120px;width:1200px;height:388px;background:linear-gradient(100deg,#0b1a2c 0%,var(--hero-a) 40%,var(--hero-b) 100%);overflow:hidden}
.hero-photo{position:absolute;left:0;top:0;width:700px;height:388px;background:linear-gradient(90deg,#0a0f18 0%,#3b4a5c 50%,#8ba6c4 75%,rgba(40,80,120,0) 100%);clip-path:polygon(0 0,100% 0,74% 100%,0 100%)}
.hero-rule{position:absolute;left:0;bottom:0;width:1200px;height:4px;background:#0b1a2c}
.hero-title{position:absolute;left:717px;top:70px;width:440px;font-size:17px;font-weight:700;line-height:22px;color:var(--royal);text-transform:uppercase}
.hero-copy{position:absolute;left:721px;top:140px;width:420px;font-size:13.5px;line-height:34px;color:var(--white)}
.btn{position:absolute;display:flex;align-items:center;justify-content:center;font-size:12px;font-weight:600;border-radius:7px}
.btn-join{left:725px;top:258px;width:181px;height:48px;background:var(--navy);color:var(--white)}
.btn-ebook{left:923px;top:258px;width:180px;height:48px;background:var(--white);color:var(--ink)}

/* how it works */
.how-works{position:absolute;left:0;top:508px;width:1200px;height:640px;background:var(--grey-bg)}
.section-title{font-size:28px;font-weight:700;color:var(--ink)}
.how-title{position:absolute;left:200px;top:76px}
.how-rule{position:absolute;left:202px;top:119px;width:142px;height:4px;background:var(--navy)}
.how-block{position:absolute;left:202px;width:395px}
.how-block h3{font-size:18px;font-weight:700;color:var(--indigo);margin-bottom:6px;white-space:nowrap}
.how-block p{font-size:9.5px;line-height:15px;color:var(--muted)}
.stats-card{position:absolute;left:605px;top:62px;width:388px;height:550px;border-radius:6px;background:radial-gradient(circle at 40% 30%,#3a86d1 0%,#1f63b0 55%,#174e92 100%);box-shadow:0 3px 8px rgba(0,0,0,.3);overflow:hidden}
.stat-icon{position:absolute;left:144px;width:104px;height:104px;border-radius:50%;background:#22364f;display:flex;align-items:center;justify-content:center}
.stat-label{position:absolute;left:0;width:388px;text-align:center;font-family:"Orbitron",sans-serif;font-size:18px;font-weight:700;color:#23354c;white-space:nowrap}

/* learn */
.learn{position:absolute;left:0;top:1187px;width:1200px;height:516px;background:var(--sky)}
.learn-head{position:absolute;left:420px;top:20px;display:flex;align-items:center;gap:10px;font-size:21px;font-weight:700}
.learn-rule{position:absolute;left:537px;top:73px;width:116px;height:4px;background:var(--navy)}
.learn-photo{position:absolute;width:219px;height:159px;box-shadow:0 2px 6px rgba(0,0,0,.3)}
.learn-item{position:absolute;width:150px}
.learn-item h4{font-size:14px;font-weight:500;color:var(--navy);margin:4px 0 3px}
.learn-item p{font-size:8px;line-height:12px;color:#3c4d85}
.learn-btn{display:inline-flex;align-items:center;justify-content:center;margin-top:8px;width:72px;height:24px;border-radius:5px;background:var(--navy);color:var(--white);font-size:8px;font-weight:600}

/* courses */
.courses{position:absolute;left:0;top:1703px;width:1200px;height:508px;background:var(--white)}
.courses-head{position:absolute;left:498px;top:32px;display:flex;align-items:center;gap:8px;font-size:20px;font-weight:700}
.courses-rule{position:absolute;left:578px;top:71px;width:40px;height:4px;background:var(--navy)}
.course-card{position:absolute;background:var(--white);border:3px solid var(--card-border);border-radius:10px;box-shadow:3px 4px 0 #4a4a6a;overflow:hidden}
.course-art{width:100%}
.course-body{padding:8px 8px}
.price{font-size:12px;font-weight:600}
.course-name{font-size:11px;font-weight:700;line-height:14px;margin-top:5px}
.course-desc{font-size:7.5px;line-height:11px;color:var(--muted);margin-top:6px}
.course-btn{display:flex;align-items:center;justify-content:center;margin:8px auto 0;width:100px;height:24px;border-radius:7px;background:var(--navy);color:var(--white);font-size:9px;font-weight:600}
.arrow{position:absolute;width:54px;height:54px;border-radius:50%;background:#393779;display:flex;align-items:center;justify-content:center}

/* footer */
.site-footer{position:absolute;left:0;top:2211px;width:1200px;height:133px;background:var(--sky)}
.featured{position:absolute;left:204px;top:16px;width:160px;text-align:center;font-family:"Orbitron",sans-serif;font-size:27px;font-weight:700;line-height:31px;color:var(--royal)}
.partner{position:absolute;top:56px;display:flex;align-items:center;gap:7px;font-size:17px;font-weight:700;color:#2a2a3a;white-space:nowrap}
.partner i{display:block;width:18px;height:18px;border-radius:50%;background:#2a2a3a}
.copyright{position:absolute;left:0;top:117px;width:1200px;text-align:center;font-family:"Orbitron",sans-serif;font-size:10px;color:#a9c4e4}
</style>
</head>
<body>

<header class="site-header">
  <div class="top-strip"></div>
  <div class="account-bar">
    <span class="account-link" style="left:136px">
      <svg width="16" height="16" viewBox="0 0 16 16" fill="none" stroke="#fff" stroke-width="1.6"><circle cx="8" cy="5" r="3.2"/><path d="M2 15c0-3.3 2.7-5.5 6-5.5s6 2.2 6 5.5"/></svg>MY ACCOUNT</span>
    <span class="account-link" style="left:325px">
      <svg width="16" height="16" viewBox="0 0 16 16" fill="none" stroke="#fff" stroke-width="1.6"><path d="M2 8h8M7 5l3 3-3 3M11 2h3v12h-3"/></svg>LOG IN</span>
  </div>
  <div class="brand"><span class="brand-dot"></span>Quiz Marlow</div>
  <nav class="main-nav">
    <span>START HERE</span><span class="current">COURSES</span><span>LABS</span><span>PRACTICE EXAMS</span><span>EXAM VOUCHERS</span><span>BOOKS</span><span>ARTICLES</span><span>ABOUT US</span>
  </nav>
</header>

<section class="hero">
  <div class="hero-photo" role="img" aria-label="Side portrait of a student in blue-tinted light"></div>
  <h1 class="hero-title">Get your ServiceFrame® v3 Foundations certification in fastest way</h1>
  <p class="hero-copy">This site will cover just the essentials with no fluff, filler, or extra material, so you can learn the material quickly and conquer the certification exam with ease.</p>
  <span class="btn btn-join">Join Now</span>
  <span class="btn btn-ebook">Get Your Free eBook Today</span>
  <div class="hero-rule"></div>
</section>

<section class="how-works">
  <h2 class="section-title how-title">How Quiz Marlow Works</h2>
  <div class="how-rule"></div>
  <div class="how-block" style="top:152px">
    <h3>Learning ServiceFrame® v3 Foundations</h3>
    <p>This site gives you a crash course that introduces everything you need to pass the ServiceFrame v3 Foundations exam. We cover just the essentials with no fluff or filler, so you learn the material quickly and conquer the exam with ease.</p>
  </div>
  <div class="how-block" style="top:286px;left:198px">
    <h3>ServiceFrame® v3 Foundations Certification</h3>
    <p>We assume you have no previous experience with the ServiceFrame v3 framework and teach the bare minimum you need to pass on your first attempt. We do not try to teach everything, such as how to implement it in your organization. This site helps you pass the exam, not become an expert.</p>
  </div>
  <div class="how-block" style="top:446px">
    <h3>Support</h3>
    <p>Get one-on-one support from experts that truly want to help you.</p>
  </div>
  <div class="how-block" style="top:506px">
    <h3>Don't Stress. Get Certified.</h3>
    <p>We move at a very quick pace through the material. If you read our material on this site or in our book and take our practice exams (scoring at least an 85% or higher), you will be ready to take and pass the ServiceFrame v3 Foundations exam on your first attempt!</p>
  </div>

  <div class="stats-card" role="img" aria-label="Blue world map background with student statistics">
    <div class="stat-icon" style="top:30px">
      <svg width="56" height="44" viewBox="0 0 56 44" fill="#fff"><circle cx="28" cy="11" r="8"/><circle cx="12" cy="15" r="6"/><circle cx="44" cy="15" r="6"/><path d="M14 44c0-10 6-17 14-17s14 7 14 17z"/><path d="M0 40c0-8 5-13 12-13 3 0 5 1 7 2-4 4-6 9-6 11z"/><path d="M56 40c0-8-5-13-12-13-3 0-5 1-7 2 4 4 6 9 6 11z"/></svg>
    </div>
    <div class="stat-label" style="top:150px">39,500+ Student Worldwide</div>
    <div class="stat-icon" style="top:212px">
      <svg width="84" height="84" viewBox="0 0 84 84"><circle cx="42" cy="42" r="36" fill="none" stroke="#1f63b0" stroke-width="8"/><path d="M34 26l24 16-24 16z" fill="#1f63b0"/></svg>
    </div>
    <div class="stat-label" style="top:332px">1,000,000+ Minutes Watched</div>
    <svg class="abs" style="left:160px;top:384px" width="68" height="88" viewBox="0 0 68 88"><rect x="2" y="2" width="64" height="84" fill="none" stroke="#22364f" stroke-width="4"/><rect x="12" y="14" width="44" height="6" fill="#22364f"/><rect x="12" y="30" width="44" height="4" fill="#22364f"/><rect x="12" y="42" width="44" height="4" fill="#22364f"/><rect x="12" y="54" width="44" height="4" fill="#22364f"/><rect x="12" y="66" width="30" height="4" fill="#22364f"/></svg>
    <div class="stat-label" style="top:488px">5,000+ Books Sold</div>
  </div>
</section>

<section class="learn">
  <div class="learn-head">
    <svg width="50" height="56" viewBox="0 0 50 56" fill="none" stroke="#fff" stroke-width="3"><path d="M25 14c-8 0-13 6-13 12 0 5 3 8 5 11v6h16v-6c2-3 5-6 5-11 0-6-5-12-13-12z"/><path d="M19 48h12M21 53h8"/><path d="M25 2v6M8 9l4 4M42 9l-4 4M2 26h6M42 26h6"/></svg>
    How You Learn From Us
  </div>
  <div class="learn-rule"></div>

  <div class="learn-photo" style="left:208px;top:118px;background:linear-gradient(135deg,#d9dde2,#7c8aa0 60%,#3d3b3e)" role="img" aria-label="Laptop playing a video lesson, held in hand"></div>
  <div class="learn-item" style="left:442px;top:124px">
    <svg width="44" height="38" viewBox="0 0 44 38" fill="#2b2a6a"><rect x="0" y="3" width="30" height="32" rx="2"/><path d="M31 13l13-9v30l-13-9z"/></svg>
    <h4>Videos</h4>
    <p>Using our Quiz Marlow video series, we take complicated certification exams and teach you to pass within a few hours.</p>
    <span class="learn-btn">Get Started</span>
  </div>

  <div class="learn-photo" style="left:620px;top:118px;background:linear-gradient(135deg,#4a3a32,#8a6a55 45%,#3b5c8a 70%,#2a2a34)" role="img" aria-label="Hand holding a study guide book in a library"></div>
  <div class="learn-item" style="left:855px;top:124px">
    <svg width="34" height="44" viewBox="0 0 34 44" fill="none" stroke="#2b2a6a" stroke-width="3"><rect x="2" y="2" width="30" height="40"/><path d="M8 10h18M8 18h18M8 25h18M8 32h12"/></svg>
    <h4>Books</h4>
    <p>Our Quiz Marlow book series will get you certified in the shortest amount of time. Learn what you need to get certified today!</p>
    <span class="learn-btn">Get Started</span>
  </div>

  <div class="learn-photo" style="left:208px;top:319px;background:linear-gradient(160deg,#c8a7c0,#9c6e70 45%,#3a2c2a)" role="img" aria-label="Phone showing a quiz app held outdoors"></div>
  <div class="learn-item" style="left:442px;top:318px">
    <svg width="28" height="50" viewBox="0 0 28 50" fill="none" stroke="#2b2a6a" stroke-width="3"><rect x="2" y="2" width="24" height="46" rx="4"/><path d="M10 42h8"/></svg>
    <h4>Apps</h4>
    <p>Our quiz apps prepare you for the certification exam while on the go. Each question comes with a complete explanation.</p>
    <span class="learn-btn">Get Started</span>
  </div>

  <div class="learn-photo" style="left:620px;top:319px;background:linear-gradient(135deg,#5b5f66,#b9bcc0 50%,#e6e4df)" role="img" aria-label="Person reading articles on a tablet beside a coffee cup"></div>
  <div class="learn-item" style="left:855px;top:322px">
    <svg width="52" height="42" viewBox="0 0 52 42" fill="none" stroke="#2b2a6a" stroke-width="3"><path d="M2 14L26 3l24 11-24 11z"/><path d="M12 19v11c4 4 9 5 14 5s10-1 14-5V19"/><path d="M46 16v14"/></svg>
    <h4>Blogs</h4>
    <p>Signup for your daily dose of training with our constantly updated blog feed of new content to learn quickly.</p>
    <span class="learn-btn">Get Started</span>
  </div>
</section>

<section class="courses">
  <div class="courses-head">
    <svg width="54" height="34" viewBox="0 0 54 34" fill="#2b2a6a"><path d="M0 11L27 0l27 11-27 11z"/><path d="M11 17v9c5 5 11 7 16 7s11-2 16-7v-9l-16 7z"/></svg>
    Courses
  </div>
  <div class="courses-rule"></div>

  <span class="arrow" style="left:203px;top:242px"><svg width="14" height="18" viewBox="0 0 14 18" fill="none" stroke="#fff" stroke-width="2"><path d="M10 3L4 9l6 6"/></svg></span>
  <span class="arrow" style="left:915px;top:242px"><svg width="14" height="18" viewBox="0 0 14 18" fill="none" stroke="#fff" stroke-width="2"><path d="M4 3l6 6-6 6"/></svg></span>

  <article class="course-card" style="left:283px;top:149px;width:171px;height:262px">
    <div class="course-art" style="height:92px;background:linear-gradient(135deg,#4a6f8e,#8fb0c8)" role="img" aria-label="ProjectGuide Foundation course badge"></div>
    <div class="course-body">
      <div class="price">$299</div>
      <div class="course-name">ProjectGuide Foundation (Exam Voucher)</div>
      <p class="course-desc">Purchase your discounted ProjectGuide Foundation exam voucher directly from Velkor Learning.</p>
      <span class="course-btn">View Course</span>
    </div>
  </article>

  <article class="course-card" style="left:473px;top:97px;width:232px;height:356px">
    <div class="course-art" style="height:140px;background:linear-gradient(135deg,#2f6fa8,#6a9cc8 50%,#9ab8d4)" role="img" aria-label="Collage of certification course tiles for full access plan"></div>
    <div class="course-body" style="padding:10px 12px">
      <div class="price" style="font-size:16px">$9 / month</div>
      <div class="course-name" style="font-size:15px;line-height:20px;margin-top:16px">Full Access to All Our Courses</div>
      <p class="course-desc" style="font-size:11px;line-height:18px;color:#444">With our $9/month plan, you get unlimited aces to all our courses!</p>
      <span class="course-btn" style="width:136px;height:36px;font-size:12px;margin-top:14px">View Course</span>
    </div>
  </article>

  <article class="course-card" style="left:723px;top:149px;width:171px;height:262px">
    <div class="course-art" style="height:92px;background:linear-gradient(135deg,#1f3346,#4d6a82)" role="img" aria-label="ServiceFrame Foundation course badge"></div>
    <div class="course-body">
      <div class="price">$299</div>
      <div class="course-name">ServiceFrame Foundation (Exam Voucher)</div>
      <p class="course-desc">Purchase your discounted ServiceFrame Foundation exam voucher directly from Velkor Learning.</p>
      <span class="course-btn">View Course</span>
    </div>
  </article>
</section>

<footer class="site-footer">
  <div class="featured">As Featured On ...</div>
  <span class="partner" style="left:404px"><i></i>Lernova</span>
  <span class="partner" style="left:536px"><i></i>Viewstream</span>
  <span class="partner" style="left:690px"><i></i>Linkwise Learning</span>
  <span class="partner" style="left:904px">Zorvel</span>
  <div class="copyright">© Copyright Quiz Marlow 2018</div>
</footer>

</body>
</html>
```